Accounting firm needing business card / letterhead designed
Marcus T. Elbering, CPA
marcus@fernquill.com
www.fernquill.com
482 N Harlow Ave Larkfield, ST 43719
555-555-0172

```html
<!DOCTYPE html>
<html lang="en">
<head>
<meta charset="utf-8">
<title>Fernquill Advisors – Business Card</title>
<link rel="stylesheet" href="https://fonts.googleapis.com/css2?family=Quicksand:wght@500;600;700&display=swap">
<style>
  :root {
    --backdrop: #dcdde2;
    --paper: #f7f7f8;
    --navy: #1f1f5c;
    --violet: #3e3672;
    --lime: #7dc242;
    --edge: #3aa3d6;
    --ink: #1b1b1b;
    --on-violet: #ffffff;
  }
  * { margin: 0; padding: 0; box-sizing: border-box; }
  html, body { width: 1200px; height: 878px; overflow: hidden; }
  body {
    background: var(--backdrop);
    font-family: "Quicksand", sans-serif;
    position: relative;
  }
  .card {
    position: absolute;
    width: 560px;
    height: 320px;
    background: var(--paper);
    box-shadow: 0 6px 18px rgba(0,0,0,.14);
    overflow: hidden;
  }
  .card--front { left: 80px; top: 90px; border-bottom: 4px solid var(--edge); }
  .card--back  { left: 560px; top: 468px; display: flex; }

  .front-brand {
    position: absolute; inset: 0;
    display: flex; align-items: center; justify-content: center;
  }
  .brand-name {
    color: var(--navy);
    font-weight: 700;
    text-transform: uppercase;
    letter-spacing: 2px;
    line-height: 1.05;
    text-align: center;
  }
  .card--front .brand-name { font-size: 50px; }

  .back-identity {
    position: relative;
    width: 50%;
    border-left: 14px solid var(--violet);
    padding: 70px 0 0 24px;
  }
  .back-identity .brand-name { font-size: 28px; text-align: left; letter-spacing: 1px; }
  .holder-name {
    margin-top: 48px;
    font-size: 16px;
    font-weight: 600;
    color: var(--ink);
    white-space: nowrap;
  }
  .divider-stripe {
    width: 12px;
    flex: none;
    background: repeating-linear-gradient(90deg, var(--lime) 0 4px, #a6d86f 4px 6px, var(--lime) 6px 12px);
  }
  .back-contact {
    flex: 1;
    background: var(--violet);
    color: var(--on-violet);
    padding: 48px 14px 0 20px;
    font-size: 13px;
    font-weight: 500;
  }
  .contact-list { list-style: none; }
  .contact-item { display: flex; align-items: flex-start; gap: 9px; margin-bottom: 8px; white-space: nowrap; }
  .contact-item--address { margin-top: 46px; line-height: 1.35; }
  .contact-icon { width: 15px; height: 15px; flex: none; margin-top: 1px; }
</style>
</head>
<body>
  <section class="card card--front" aria-label="Business card front">
    <div class="front-brand">
      <p class="brand-name">Fernquill<br>Advisors</p>
    </div>
  </section>

  <section class="card card--back" aria-label="Business card back">
    <div class="back-identity">
      <p class="brand-name">Fernquill<br>Advisors</p>
      <p class="holder-name">Marcus T. Elbering, CPA</p>
    </div>
    <div class="divider-stripe"></div>
    <div class="back-contact">
      <ul class="contact-list">
        <li class="contact-item">
          <svg class="contact-icon" viewBox="0 0 16 16"><circle cx="8" cy="8" r="8" fill="#fff"/><path d="M5 4.5l1.6-.3.8 2-1 .7a5 5 0 0 0 2.7 2.7l.7-1 2 .8-.3 1.6c-3.7.3-6.8-2.8-6.5-6.5z" fill="#3e3672"/></svg>
          <span>555-555-0172</span>
        </li>
        <li class="contact-item">
          <svg class="contact-icon" viewBox="0 0 16 16"><circle cx="8" cy="8" r="8" fill="#fff"/><circle cx="8" cy="8" r="4.5" fill="none" stroke="#3e3672" stroke-width="1.1"/><path d="M3.5 8h9M8 3.5c-2 2.5-2 6.5 0 9M8 3.5c2 2.5 2 6.5 0 9" fill="none" stroke="#3e3672" stroke-width="1"/></svg>
          <span>www.fernquill.com</span>
        </li>
        <li class="contact-item">
          <svg class="contact-icon" viewBox="0 0 16 16"><circle cx="8" cy="8" r="8" fill="#fff"/><rect x="4" y="5.2" width="8" height="5.6" fill="none" stroke="#3e3672" stroke-width="1.1"/><path d="M4 5.4l4 3 4-3" fill="none" stroke="#3e3672" stroke-width="1.1"/></svg>
          <span>marcus@fernquill.com</span>
        </li>
        <li class="contact-item contact-item--address">
          <svg class="contact-icon" viewBox="0 0 16 16"><circle cx="8" cy="8" r="8" fill="#fff"/><path d="M8 12.5S4.8 9.2 4.8 7a3.2 3.2 0 0 1 6.4 0c0 2.2-3.2 5.5-3.2 5.5z" fill="#3e3672"/><circle cx="8" cy="7" r="1.2" fill="#fff"/></svg>
          <span>482 N Harlow Ave Larkfield<br>ST 43719</span>
        </li>
      </ul>
    </div>
  </section>
</body>
</html>
```